Welbourne Dental, P.C. New stationary and business card for modern Dental Office

We need a new stationary/envelope/business card design using our newly designed logo. We are looking for an upscale look. Our new logo is used on our signage, using black as the background and white for the lettering. We would like the stationary to have black, white, possible greys or silver. We are looking for a letterhead, envelope, and business card design for three different employees, as well as a 4th card, same design, but just general with no employee name.

Project Deadline Extended
Reason: We began this project in the middle of our move into our new office. Things got pretty hectic and we just didn't have the time to go through designs. We now settled in and finally eliminated the designs that didn't work for us. We would like to extend the project another 5 days, and then finalize our decision. Most of the submissions showed business cards alone, with no stationary designs. Our original request was for stationary and business cards. Please keep this in mind.

Target Market(s)

Dental patients expecting high quality, cosmetic dentistry

Industry/Entity Type

Business

Contact Information for Business Card

Will need a design using our logo. All cards will be the same, other than that one card will have Office Managers name, One for the Doctor, Hygienist,
1. Office Manager - Marisol Dubrovka
2. Hygienist - Kayleigh Morrow
3. Gordon T. Welbourne, D.D.S.
4. One general one with no staff names

Font styles to use
Other font styles liked:
• see upload

Colors
000000
1b1b1b
757575
c9c9c9
e8e8e8
ffffff

Requirements
Must have
• -Logo
• -Phone number (718)555-0193
• -Address: 4352 63rd Ave
• Lower Level
• Brooklyn, NY 11290

```html
<!DOCTYPE html>
<html lang="en">
<head>
<meta charset="utf-8">
<title>Welbourne Dental, P.C. — Business Card</title>
<link rel="stylesheet" href="https://fonts.googleapis.com/css2?family=Tinos:ital,wght@0,400;0,700;1,400&display=swap">
<style>
  :root {
    --ink: #000000;
    --ink-soft: #1b1b1b;
    --steel: #757575;
    --silver: #c9c9c9;
    --mist: #e8e8e8;
    --paper: #ffffff;
  }
  html, body {
    margin: 0;
    padding: 0;
    width: 1200px;
    height: 685px;
    overflow: hidden;
    background: var(--paper);
  }
  .card {
    position: relative;
    width: 1200px;
    height: 685px;
    background: var(--paper);
    font-family: "Tinos", "Times New Roman", serif;
    color: var(--ink);
  }
  .person {
    position: absolute;
    left: 0;
    width: 608px;
    text-align: center;
  }
  .person-name {
    top: 208px;
    margin: 0;
    font-size: 64px;
    font-weight: 700;
    line-height: 1;
  }
  .person-title {
    top: 314px;
    margin: 0;
    font-size: 31px;
    font-style: italic;
    letter-spacing: 2px;
    line-height: 1;
  }
  .person-email {
    top: 546px;
    margin: 0;
    font-size: 29px;
    font-weight: 700;
    letter-spacing: 2.5px;
    line-height: 1;
  }
  .divider {
    position: absolute;
    top: 84px;
    height: 518px;
  }
  .divider-silver {
    left: 580px;
    width: 8px;
    background: var(--steel);
    opacity: 0.75;
  }
  .divider-black {
    left: 600px;
    width: 5px;
    background: var(--ink);
  }
  .practice-name {
    position: absolute;
    left: 670px;
    top: 112px;
    margin: 0;
    font-size: 44px;
    font-weight: 700;
    color: var(--steel);
    white-space: nowrap;
    line-height: 1;
  }
  .address {
    position: absolute;
    left: 706px;
    top: 408px;
    margin: 0;
    font-style: normal;
    font-size: 34px;
    line-height: 45px;
    color: var(--ink);
  }
</style>
</head>
<body>
  <main class="card">
    <h1 class="person person-name">Jonah Pell</h1>
    <p class="person person-title">Title</p>
    <p class="person person-email">jonah@welbourne.com</p>

    <div class="divider divider-silver" aria-hidden="true"></div>
    <div class="divider divider-black" aria-hidden="true"></div>

    <p class="practice-name">Welbourne Dental, P.C.</p>

    <address class="address">
      4352 63rd Ave<br>
      Lower Level<br>
      Brooklyn, NY 11290<br>
      (718)555-0193
    </address>
  </main>
</body>
</html>
```